Postcard Design

We are Thessaly Pages based on Oxford, UK. We sell rare and collectible books and we want to include an attractive postcard with the order. This is seen as having several functions: a thank you for buying from us, a functional item that can be used as a book mark, a reminder of how to contact us and browse our ever-changing stock at www.thessalypages.co.uk (please note the website is off-line at the moment for some major improvements).

We like clean and simple designs. We pride ourselves on the quality of our stock, our honest appraisals of the condition of our books and our no-quibble guarantee - if the buyer is unhappy for any reason we will give a full refund (including postage) on safe return of the item.

Requirements
Must have
• website address (www.thessalypages.co.uk)

```html
<!DOCTYPE html>
<html lang="en">
<head>
<meta charset="utf-8">
<title>Thessaly Pages – Thank You Postcard</title>
<link rel="stylesheet" href="https://fonts.googleapis.com/css2?family=Libre+Baskerville:wght@400;700&display=swap">
<style>
  :root {
    --brand-red: #a0282a;
    --accent-red: #c0392b;
    --ink: #222222;
    --paper: #ffffff;
    --cream: #efe3c6;
    --bezel: #111111;
    --laptop-base: #c9cbce;
    --shelf-dark: #3a2418;
    --shelf-mid: #8a4a26;
    --shelf-light: #b88a4a;
    --wall: #8c8a86;
  }
  * { margin: 0; padding: 0; box-sizing: border-box; }
  html, body { width: 1200px; height: 925px; overflow: hidden; background: var(--paper); }
  .postcard {
    position: relative; width: 1200px; height: 925px;
    background: var(--paper);
    font-family: "Libre Baskerville", Georgia, serif;
    color: var(--ink);
  }
  .book-photo {
    position: absolute; left: 0; top: 118px; width: 1200px; height: 454px;
    background:
      linear-gradient(90deg, var(--shelf-dark) 0%, var(--shelf-mid) 16%, var(--shelf-light) 27%, var(--shelf-dark) 33%, var(--shelf-dark) 49%, var(--shelf-mid) 55%, var(--accent-red) 63%, var(--shelf-mid) 72%, var(--shelf-light) 80%, var(--wall) 96%);
  }
  .thanks-ribbon { position: absolute; left: 0; top: 18px; width: 662px; height: 112px; }
  .thanks-ribbon svg { position: absolute; inset: 0; }
  .thanks-ribbon p {
    position: relative; padding: 12px 0 0 64px;
    color: var(--paper); font-size: 32px; line-height: 42px;
  }
  .thanks-ribbon p span { display: block; }
  .thanks-ribbon p span + span { padding-left: 0; margin-left: -2px; }
  .intro {
    position: absolute; left: 30px; width: 645px; text-align: center;
  }
  .intro-selection { top: 590px; font-weight: 700; font-size: 22px; line-height: 33px; }
  .intro-explore { top: 680px; color: var(--accent-red); font-weight: 700; font-size: 24px; line-height: 37px; }
  .shop-name { top: 788px; font-size: 38px; line-height: 48px; }
  .laptop { position: absolute; left: 640px; top: 527px; width: 535px; height: 311px; }
  .laptop-screen {
    position: absolute; left: 50px; top: 0; width: 435px; height: 295px;
    background: var(--bezel); border-radius: 14px 14px 0 0; padding: 18px 15px 0;
  }
  .screen-content { width: 100%; height: 258px; position: relative; background: var(--cream); overflow: hidden; }
  .screen-heading { height: 33px; text-align: center; font-size: 16px; line-height: 33px; color: var(--ink); }
  .screen-shelf {
    height: 130px;
    background: linear-gradient(90deg, #3b2a1e 0%, #6b4a2c 30%, #7a5030 50%, #5b6a3a 70%, #3e4a2a 100%);
  }
  .screen-url {
    position: absolute; left: 0; right: 0; top: 108px; text-align: center;
    color: var(--paper); font-size: 22px;
  }
  .screen-button {
    position: absolute; left: 120px; top: 190px; width: 162px; height: 37px;
    background: var(--brand-red); color: var(--paper);
    font-size: 17px; line-height: 37px; text-align: center;
  }
  .laptop-base {
    position: absolute; left: 0; top: 293px; width: 535px; height: 16px;
    background: linear-gradient(var(--laptop-base), #8e9094); border-radius: 2px 2px 10px 10px;
  }
  .web-band {
    position: absolute; left: 0; top: 850px; width: 1200px; height: 75px;
    background: var(--brand-red); color: var(--paper);
    text-align: center; font-size: 42px; line-height: 75px;
  }
</style>
</head>
<body>
<main class="postcard">
  <div class="book-photo" role="img" aria-label="Photograph of antique leather-bound books with gilt spines standing on a shelf"></div>

  <div class="thanks-ribbon">
    <svg width="662" height="112" viewBox="0 0 662 112" aria-hidden="true">
      <polygon points="0,0 662,0 630,56 662,112 0,112" fill="var(--brand-red)"/>
      <line x1="0" y1="5" x2="659" y2="5" stroke="#ffffff" stroke-opacity="0.35" stroke-width="1"/>
    </svg>
    <p><span>Thank you for your purchase!</span><span>Keep buying from Thessaly Pages.</span></p>
  </div>

  <p class="intro intro-selection">We have the largest selection of Rare, Limited<br>Editions and collectable books in Oxford.</p>
  <p class="intro intro-explore">Explore and order our latest exclusive<br>Collection of books at</p>
  <p class="intro shop-name">Thessaly Pages</p>

  <div class="laptop">
    <div class="laptop-screen">
      <div class="screen-content">
        <p class="screen-heading">Limited Editions</p>
        <div class="screen-shelf" role="img" aria-label="Row of leather-bound book spines"></div>
        <p class="screen-url">www.thessalypages.co.uk</p>
        <p class="screen-button">BUY NOW</p>
      </div>
    </div>
    <div class="laptop-base"></div>
  </div>

  <footer class="web-band">www.thessalypages.co.uk</footer>
</main>
</body>
</html>
```